A Speech Therapy Business needs to update their logo

I need an update to the font and color of my logo to look more appealing. I am looking to open a private practice as a Speech Language Pathologist that caters to adults and children. It needs to be sophisticated and friendly at the same time. I want to keep the silhouette in my logo as is, just update the font and color for "Brightpath".
Industry/Entity Type
Business
Contact Information for Business Card
I want the business card to have my logo, my name (Odile Varn, CCC-SLP, TSSLD) and that I am a Bilingual Speech Language Pathologist. Also, include my phone number, (718) 555-0193. Include my website, Brightpathslp.example, and email address, odilevarn@brightpathslp.example
Look and feel

```html
<!DOCTYPE html>
<html lang="en">
<head>
<meta charset="utf-8">
<title>Brightpath – Business Card</title>
<link href="https://fonts.googleapis.com/css2?family=Open+Sans:wght@400;600;700&display=swap" rel="stylesheet">
<style>
  :root {
    --page-bg: #e9ecef;
    --card-bg: #ffffff;
    --brand-blue: #2391d0;
    --band-blue: #2a93d1;
    --text-dark: #3a3d42;
    --text-muted: #55595f;
    --silhouette: #1d1d1f;
  }
  * { margin: 0; padding: 0; box-sizing: border-box; }
  html, body {
    width: 1200px;
    height: 1000px;
    overflow: hidden;
    background: var(--page-bg);
    font-family: "Open Sans", sans-serif;
  }
  .business-card {
    position: absolute;
    left: 100px;
    top: 230px;
    width: 1000px;
    height: 540px;
    background: var(--card-bg);
    box-shadow: 0 6px 24px rgba(0,0,0,0.12);
    overflow: hidden;
  }
  .band-top, .band-bottom {
    position: absolute;
    left: 0;
    width: 100%;
    background: var(--band-blue);
  }
  .band-top { top: 0; height: 32px; }
  .band-bottom { bottom: 0; height: 26px; }

  .identity {
    position: absolute;
    left: 46px;
    top: 98px;
    padding-left: 32px;
  }
  .identity::before {
    content: "";
    position: absolute;
    left: 0;
    top: 8px;
    width: 11px;
    height: 60px;
    background: var(--brand-blue);
  }
  .person-name {
    font-size: 40px;
    font-weight: 700;
    color: var(--brand-blue);
    line-height: 1.1;
    letter-spacing: 0.3px;
  }
  .credentials {
    font-size: 21px;
    font-weight: 600;
    color: var(--text-dark);
    margin-top: 2px;
    letter-spacing: 0.5px;
  }

  .contact-list {
    position: absolute;
    left: 46px;
    top: 336px;
    list-style: none;
  }
  .contact-item {
    display: flex;
    align-items: center;
    height: 32px;
    font-size: 21px;
    color: var(--text-muted);
  }
  .contact-icon {
    width: 22px;
    height: 22px;
    margin-right: 26px;
    flex: none;
  }

  .brand-mark {
    position: absolute;
    left: 545px;
    top: 222px;
    width: 400px;
  }
  .family-silhouette {
    width: 395px;
    height: 118px;
    background: linear-gradient(90deg, var(--silhouette), #3a3a3c);
    border-radius: 4px;
    opacity: 0.9;
  }
  .brand-name {
    font-size: 54px;
    font-weight: 400;
    color: var(--brand-blue);
    line-height: 1;
    margin-top: 4px;
    margin-left: 8px;
  }
</style>
</head>
<body>
  <section class="business-card">
    <div class="band-top"></div>

    <header class="identity">
      <h1 class="person-name">Odile Varn</h1>
      <p class="credentials">CCC-SLP,TSSLD</p>
    </header>

    <ul class="contact-list">
      <li class="contact-item">
        <svg class="contact-icon" viewBox="0 0 24 24" aria-hidden="true">
          <rect x="7" y="2" width="10" height="20" rx="2" fill="none" stroke="var(--brand-blue)" stroke-width="2"/>
          <circle cx="12" cy="18" r="1.2" fill="var(--brand-blue)"/>
        </svg>
        (718) 555-0193
      </li>
      <li class="contact-item">
        <svg class="contact-icon" viewBox="0 0 24 24" aria-hidden="true">
          <rect x="2" y="5" width="20" height="14" rx="1.5" fill="none" stroke="var(--brand-blue)" stroke-width="2"/>
          <path d="M2.5 6 L12 13 L21.5 6" fill="none" stroke="var(--brand-blue)" stroke-width="2"/>
        </svg>
        odilevarn@brightpathslp.example
      </li>
      <li class="contact-item">
        <svg class="contact-icon" viewBox="0 0 24 24" aria-hidden="true">
          <circle cx="12" cy="12" r="9.5" fill="none" stroke="var(--brand-blue)" stroke-width="2"/>
          <ellipse cx="12" cy="12" rx="4" ry="9.5" fill="none" stroke="var(--brand-blue)" stroke-width="1.6"/>
          <line x1="2.5" y1="12" x2="21.5" y2="12" stroke="var(--brand-blue)" stroke-width="1.6"/>
        </svg>
        www.brightpathslp.example
      </li>
    </ul>

    <div class="brand-mark">
      <div class="family-silhouette" role="img" aria-label="Silhouette of a family walking hand in hand, from adults down to small children, ending with a small heart"></div>
      <p class="brand-name">Brightpath</p>
    </div>

    <div class="band-bottom"></div>
  </section>
</body>
</html>
```